Lantern Business Cards

Need business cards for my employees at my restaurant.

Needs to include:
Our Logo
Lantern Bowls & Brews
Name: Nora Pettigrew
Title : Owner
Address: 487 Mirella Ave. Cedar Hollow, NV 86519
Web: www.lanternkestrel.com
Phone: 541-555-0147
Cell: 541-555-0192
Email: info@lanternkestrel.com

```html
<!DOCTYPE html>
<html lang="en">
<head>
<meta charset="utf-8">
<title>Lantern Bowls &amp; Brews — Business Cards</title>
<link href="https://fonts.googleapis.com/css2?family=Montserrat:wght@400;500;700&display=swap" rel="stylesheet">
<style>
  :root{
    --page:#e6e6e6;
    --ink:#0b0b0c;
    --red:#c41e2f;
    --red-deep:#7d0f16;
    --paper:#ffffff;
    --rule:#d9d9d9;
  }
  *{margin:0;padding:0;box-sizing:border-box}
  html,body{width:1200px;height:849px;overflow:hidden;background:var(--page)}
  body{position:relative;font-family:"Montserrat",sans-serif}
  .card{position:absolute;left:290px;width:620px;height:355px;overflow:hidden;background:var(--ink)}
  .card--contact{top:44px}
  .card--brand{top:450px}
  .card__art{position:absolute;inset:0;width:100%;height:100%}

  /* contact side */
  .side-brand{position:absolute;left:102px;top:172px;width:230px;height:50px;
    transform:translate(-50%,-50%) rotate(-90deg);display:flex;align-items:center;gap:10px}
  .side-brand__mark{width:32px;height:32px;border-radius:50%;background:var(--red);flex:none}
  .side-brand__text{display:flex;flex-direction:column;align-items:flex-start}
  .side-brand__name{color:var(--red);font-weight:700;font-size:26px;letter-spacing:1px;line-height:1}
  .side-brand__tag{display:flex;align-items:center;gap:6px;color:var(--paper);font-size:6.5px;letter-spacing:.8px;margin-top:4px}
  .side-brand__tag::after{content:"";width:30px;height:1px;background:var(--paper)}
  .holder{position:absolute;right:24px;top:36px;text-align:left}
  .holder__name{color:var(--red);font-weight:500;font-size:25px;line-height:1.1;
    text-decoration:underline;text-decoration-thickness:2px;text-underline-offset:3px}
  .holder__title{color:var(--red);font-weight:500;font-size:16px;line-height:1.1}
  .contacts{position:absolute;right:22px;top:0;list-style:none}
  .contacts li{position:absolute;right:0;display:flex;align-items:center;gap:11px;white-space:nowrap;
    color:var(--red);font-size:12.2px;font-weight:500}
  .contacts svg{width:13px;height:13px;flex:none}

  /* brand side */
  .brand{position:absolute;left:0;right:0;top:100px;display:flex;flex-direction:column;align-items:center}
  .brand__mark{width:58px;height:58px;border-radius:50%;background:var(--red);margin-bottom:12px}
  .brand__name{color:var(--red);font-weight:700;font-size:44px;letter-spacing:2px;line-height:1}
  .brand__tag{display:flex;align-items:center;gap:8px;color:var(--ink);font-size:10.5px;letter-spacing:1px;margin-top:4px}
  .brand__tag::before,.brand__tag::after{content:"";width:44px;height:1px;background:var(--ink)}
</style>
</head>
<body>

<section class="card card--contact" aria-label="Contact side">
  <svg class="card__art" viewBox="0 0 586 336" preserveAspectRatio="none" aria-hidden="true">
    <rect width="586" height="336" fill="#0b0b0c"/>
    <path d="M230 0 C112 70 112 250 290 336 L586 336 L586 0 Z" fill="#ffffff"/>
    <path d="M237 0 C120 72 120 250 297 336 L586 336 L586 0 Z" fill="#c41e2f"/>
    <path d="M268 0 C150 80 140 250 312 336 L586 336 L586 0 Z" fill="#7d0f16"/>
    <path d="M276 0 C158 80 150 252 318 336 L586 336 L586 0 Z" fill="#c41e2f"/>
    <path d="M292 0 C165 60 160 270 330 336 L586 336 L586 0 Z" fill="#ffffff"/>
  </svg>

  <div class="side-brand">
    <span class="side-brand__mark"></span>
    <span class="side-brand__text">
      <span class="side-brand__name">LANTERN</span>
      <span class="side-brand__tag">BOWLS AND BREWS</span>
    </span>
  </div>

  <div class="holder">
    <p class="holder__name">Nora Pettigrew</p>
    <p class="holder__title">Owner</p>
  </div>

  <ul class="contacts">
    <li style="top:107px">541-555-0192
      <svg viewBox="0 0 14 14"><circle cx="7" cy="7" r="7" fill="#c41e2f"/><path d="M4.3 3.8c.4-.4.9-.4 1.1 0l.6 1.1c.2.3 0 .6-.2.8l-.4.3c.4.9 1.1 1.6 2 2l.3-.4c.2-.2.5-.4.8-.2l1.1.6c.4.2.4.7 0 1.1-.6.6-1.4.8-2.2.4-1.6-.8-2.7-1.9-3.5-3.5-.4-.8-.2-1.6.4-2.2z" fill="#fff"/></svg></li>
    <li style="top:139px">541-555-0147
      <svg viewBox="0 0 14 14"><circle cx="7" cy="7" r="7" fill="#c41e2f"/><rect x="5" y="3.3" width="4" height="7.4" rx=".8" fill="none" stroke="#fff" stroke-width="1"/></svg></li>
    <li style="top:172px">info@lanternkestrel.com
      <svg viewBox="0 0 14 14"><circle cx="7" cy="7" r="7" fill="#c41e2f"/><rect x="3.6" y="4.6" width="6.8" height="4.8" fill="#fff"/><path d="M3.6 4.8 7 7.3l3.4-2.5" fill="none" stroke="#c41e2f" stroke-width=".8"/></svg></li>
    <li style="top:205px">www.lanternkestrel.com
      <svg viewBox="0 0 14 14"><circle cx="7" cy="7" r="7" fill="#c41e2f"/><circle cx="7" cy="7" r="3.3" fill="none" stroke="#fff" stroke-width=".9"/><path d="M3.7 7h6.6M7 3.7c-1.6 2-1.6 4.6 0 6.6M7 3.7c1.6 2 1.6 4.6 0 6.6" fill="none" stroke="#fff" stroke-width=".7"/></svg></li>
    <li style="top:240px">487 Mirella Ave. Cedar Hollow, NV 86519
      <svg viewBox="0 0 14 14"><circle cx="7" cy="7" r="7" fill="#c41e2f"/><path d="M7 3.2a2.6 2.6 0 0 0-2.6 2.6C4.4 7.8 7 10.8 7 10.8s2.6-3 2.6-5A2.6 2.6 0 0 0 7 3.2z" fill="#fff"/><circle cx="7" cy="5.8" r="1" fill="#c41e2f"/></svg></li>
  </ul>
</section>

<section class="card card--brand" aria-label="Brand side">
  <svg class="card__art" viewBox="0 0 586 336" preserveAspectRatio="none" aria-hidden="true">
    <rect width="586" height="336" fill="#0b0b0c"/>
    <ellipse cx="288" cy="172" rx="250" ry="238" transform="rotate(-30 288 172)" fill="#c41e2f"/>
    <ellipse cx="292" cy="170" rx="243" ry="233" transform="rotate(-30 292 170)" fill="#7d0f16"/>
    <ellipse cx="294" cy="170" rx="239" ry="231" transform="rotate(-30 294 170)" fill="#c41e2f"/>
    <circle cx="297" cy="170" r="232" fill="#d9d9d9"/>
    <circle cx="298" cy="170" r="229" fill="#ffffff"/>
  </svg>

  <div class="brand">
    <span class="brand__mark"></span>
    <span class="brand__name">LANTERN</span>
    <span class="brand__tag">BOWLS AND BREWS</span>
  </div>
</section>

</body>
</html>
```